Trailmark Depot Website - Sell Outdoor product

We are a mom and pop company that just opened our website.

We need a fresh, professional, and nice looking website for our outdoor products. We sell hunting, camping, fishing, and hiking products/accessories to name a few. Some of these products are optics, gun safes, gun bi-pods and tripods, gun lights, hunting camera, tents, hearing protection, targets, fishing poles, and hiking backpacks to name a few.

Our current website is: http://www.trailmarkdepot.example . You'll see our logo on the website, and it is attached. We aren't married to this logo, so if the designer thinks they can modify it or even come up with a better design for the website, they are more than welcome to do so. We need someone with good images of their own (clip art and/or outdoor images) they can use if they need to for our website.

I also attached a idea I had in visio, but please don't think this is set in stone. It is just a very rough idea. You can also go to our bazaarly site to see what we sell: www.bazaarly.example/shops/q7xk204mzpte9r . Right now we sell everything on Bazaarly, but our website will just focus on outdoor product. So please make it an outdoor focused website. And you can be creative with some of the product category names. We also want to leave room for some parallel product in the future. Like garden tools, back yard furniture, and BBQs.

Our company also wants to include a deals section on the website. We will probably update it once a week or month. I have included what I did for a deal and accompanying images for it. Image is called Movrelsi (And the main images are 01 and 02).

We also want to make sure the file is compatible with our current web-hosting company, https://www.shopvantic.example. So I included a webpage layout zip folder. If you have any questions, please contact me.

This is for a PSD and HTML/CSS webpage. If you have any artwork or images that you own and want to use them for the webpage, please do so.

Target Market(s)

The hunter, outdoors person, camper, hiker, and etc.

Industry/Entity Type

It Company

Coding

Coded - Design and coding required

Number of Pages Required

3 page

Requirements
Must have
• The main page. PSD and HTML/CSS file.
• The category page. PSD and HTML/CSS file
• The product display page. PSD and HTML/CSS file
• Please also use some images that you have or from the sites below:
• You can get free stock images for 7 days (20 per day) from this site:
• https://www.pixorchard.example/complimentary/KXRTPLD/?utm_source=KXRTPFreeLD&utm_medium=cpc&utm_campaign=KXRTPFreeLD&gclid=ZQRn8wpMtvBDHSjLuWoeR2kBuW
• Has 14 good sites:
• http://www.venturedaily.example/article/517392
• Here are the ones I like:
• https://clearframe.example/
• http://brightwoven.example/
• http://www.sitepetal.example/free/nature
• http://www.lumivault.example/archive
• http://tinyglimpse.example/
• http://old.phrelko.example/search/hiking
• http://grabvolo.blogspace.example/
• http://kirodelane.example/post/604927315581/download
• http://openstillvault.example/
• If there is a photographer listed on or next to the image, on the bottom lower corner of the image, please put the photographer's name.
Nice to have
• I would like to have an unsubscribe page. If the designer has any of their own images of the outdoor world, and they want to use them, please do. Just make the right graphic changes to make it look good.
Should not have
• Try and keep green color to a minimum.

```html
<!DOCTYPE html>
<html lang="en">
<head>
<meta charset="utf-8">
<title>Trailmark Depot</title>
<link rel="stylesheet" href="https://fonts.googleapis.com/css2?family=Open+Sans:wght@400;600;700&display=swap">
<style>
:root{
  --yellow:#f5b800;
  --nav-line:#444;
  --ink:#333;
  --muted:#888;
  --panel:#f4f4f4;
  --green:#3d9a1c;
  --red:#e8484f;
  --olive:#7a9e3c;
  --icon:#a8a8a8;
  --footer:#2e2e2e;
  --footer-deep:#232323;
  --footer-text:#8a8a8a;
}
*{box-sizing:border-box;margin:0;padding:0}
html,body{width:737px;height:1200px;overflow:hidden}
body{position:relative;background:#fff;font-family:"Open Sans",Arial,sans-serif;color:var(--ink)}
.abs{position:absolute}
ul{list-style:none}

/* top bar */
.topbar{left:0;top:0;width:737px;height:30px;background:#f2f2f2;border-top:2px solid var(--yellow);border-bottom:1px solid #e3e3e3;font-size:7.5px;color:var(--muted)}
.topbar .label{left:61px;top:9px}
.topbar .email{left:110px;top:6px;width:102px;height:15px;background:#fff;border:1px solid #ddd;font-size:5.5px;padding:3px 6px;color:#777}
.topbar .join{left:220px;top:6px;width:49px;height:15px;background:var(--yellow);color:#fff;font-size:6.5px;text-align:center;line-height:15px}
.topbar .links{right:62px;top:9px;display:flex;gap:14px}
.topbar .links span{display:flex;align-items:center;gap:5px}
.topbar .links span+span{border-left:1px solid #ddd;padding-left:10px}

/* header */
.brand{left:0;top:30px;width:737px;height:90px;display:flex;align-items:center;justify-content:center;gap:8px}
.brand .mark{width:14px;height:14px;border-radius:50%;background:var(--yellow)}
.brand .name{font-size:22px;font-weight:700;color:#1f1f1f;letter-spacing:1px}

/* nav */
.nav{left:60px;top:120px;width:616px;height:35px;background:linear-gradient(#383838,#242424);display:flex;z-index:3;box-shadow:0 2px 4px rgba(0,0,0,.3)}
.nav a{color:#fff;font-size:7.6px;font-weight:600;text-decoration:none;display:flex;align-items:center;justify-content:center;border-right:1px solid var(--nav-line)}
.nav a.active{background:var(--yellow)}

/* hero */
.hero{left:0;top:141px;width:737px;height:313px;background:
  radial-gradient(ellipse 150px 190px at 160px 210px,rgba(214,120,40,.55),rgba(214,120,40,0) 70%),
  radial-gradient(ellipse 120px 160px at 300px 190px,rgba(70,140,200,.45),rgba(70,140,200,0) 70%),
  radial-gradient(ellipse 260px 80px at 560px 260px,rgba(70,110,40,.6),rgba(70,110,40,0) 75%),
  linear-gradient(180deg,#c9d9e6 0%,#b3c8d6 22%,#8fa6ae 40%,#7d9670 55%,#5f8540 72%,#4c7132 100%)}
.hero h1{right:63px;top:118px;font-size:25px;font-weight:600;color:#fff;letter-spacing:.5px}
.hero p{right:63px;top:157px;width:240px;text-align:right;font-size:6.6px;line-height:14px;color:#fff;font-weight:600}
.hero .shop{left:595px;top:195px;width:76px;height:24px;background:var(--yellow);color:#fff;font-size:9px;font-weight:700;text-align:center;line-height:24px}
.hero .dots{left:630px;top:293px;display:flex;gap:4px}
.hero .dots i{width:7px;height:7px;border-radius:50%;border:1.5px solid #fff}
.hero .dots i.on{background:var(--yellow)}
.shade{left:90px;top:451px;width:557px;height:30px;border-radius:50%;background:radial-gradient(ellipse at 50% 0%,rgba(0,0,0,.55),rgba(0,0,0,0) 65%)}

/* categories */
.cats{left:60px;top:478px;width:167px}
.cats .head{height:29px;background:var(--yellow);color:#fff;font-size:11px;font-weight:700;display:flex;align-items:center;gap:10px;padding-left:10px}
.cats li{height:28px;background:var(--panel);border-bottom:1px solid #e6e6e6;display:flex;align-items:center;font-size:7.8px;padding-left:9px;position:relative}
.cats li svg{width:16px;height:16px;margin-right:12px}
.cats li .go{position:absolute;right:10px;top:10px;width:7px;height:7px;border:1px solid #aaa;border-radius:50%}
.side-title{font-size:11.5px;color:#222;font-weight:400}
.brands{left:60px;top:748px;width:167px}
.brands li{font-size:6px;color:#555;height:17px;line-height:17px;border-bottom:1px solid #ececec;padding-left:19px;position:relative}
.brands li::before{content:"";position:absolute;left:8px;top:7px;width:3px;height:3px;border-radius:50%;background:#c8c8c8}
.loginbox{left:60px;top:882px;width:167px}
.loginbox .field{width:167px;height:20px;border:1px solid #ddd;font-size:6px;color:#666;padding:5px 8px;margin-top:5px}
.loginbox .field:first-of-type{margin-top:13px}
.loginbox .btn{margin-top:9px;width:48px;height:18px;background:var(--yellow);color:#fff;font-size:8px;text-align:center;line-height:18px}

/* featured */
.feat-title{left:238px;top:484px}
.feat-rule{left:367px;top:490px;width:283px;height:3px;border-top:1px dotted #ccc;border-bottom:1px dotted #ccc}
.feat-arrows{left:654px;top:486px;display:flex;gap:1px}
.feat-arrows span{width:10px;height:11px;background:#888;color:#fff;font-size:7px;line-height:11px;text-align:center}
.card{width:135px;height:181px;border:1px solid #e4e4e4;background:#fff}
.card .badge{left:11px;top:11px;width:31px;height:31px;border-radius:50%;color:#fff;font-size:7.5px;text-align:center;line-height:31px}
.card .photo{left:30px;top:12px;width:84px;height:86px}
.card .name{left:11px;top:111px;font-size:6.8px;color:#444;white-space:nowrap}
.card .desc{left:11px;top:126px;width:118px;font-size:5.6px;line-height:10px;color:#999}
.card .actions{left:0;bottom:0;width:133px;height:25px;border-top:1px solid #e4e4e4;display:flex}
.card .actions span{width:30px;border-right:1px solid #e4e4e4;display:flex;align-items:center;justify-content:center}
.card .actions svg{width:10px;height:10px}
.card .price{flex:1;color:var(--green);font-size:12px;display:flex;align-items:center;justify-content:center}
.card .price small{font-size:6px;margin-right:1px;color:#444}
.card .price sup{font-size:6px;align-self:flex-start;margin-top:5px}

.pager{left:486px;top:940px;display:flex;gap:12px;font-size:8px;font-weight:700;color:#222}
.pager .cur{color:#e33}
.pager .edge{color:#777;font-weight:400}
.pager-line{left:490px;top:956px;width:186px;height:2px;background:linear-gradient(90deg,transparent,#ddd,transparent)}

/* footer */
.footer{left:0;top:999px;width:737px;height:166px;background:var(--footer)}
.fcol{top:16px}
.fcol h3{font-size:8.5px;font-weight:600;color:#bdbdbd;margin-bottom:10px}
.fcol .links li{font-size:5.8px;color:var(--footer-text);height:14.4px;padding-left:9px;position:relative}
.fcol .links li::before{content:"";position:absolute;left:0;top:3px;width:3px;height:3px;border-radius:50%;background:#555}
.contact li{display:flex;align-items:center;gap:9px;height:21.5px;font-size:5.8px;color:var(--footer-text)}
.contact i{width:14px;height:14px;border-radius:50%;border:1px solid #555;display:flex;align-items:center;justify-content:center}
.fdivider{left:75px;top:121px;width:600px;height:1px;background:#3d3d3d}
.fnews{left:74px;top:139px;font-size:8.5px;color:#bdbdbd;font-weight:600}
.fnews-input{left:143px;top:135px;width:97px;height:18px;background:#fff;font-size:5.6px;color:#888;padding:5px 4px}
.fnews-input i{position:absolute;right:4px;top:3px;width:11px;height:11px;border-radius:50%;background:#2b4a8c}
.follow{left:470px;top:139px;font-size:8.5px;color:#bdbdbd;font-weight:600}
.socials{left:530px;top:133px;display:flex;gap:4px}
.socials i{width:21px;height:21px;border-radius:50%}
.copy{left:0;top:1165px;width:737px;height:35px;background:var(--footer-deep);color:#ddd;font-size:6px;text-align:center;line-height:34px;border-bottom:2px solid var(--yellow)}
</style>
</head>
<body>

<svg width="0" height="0" style="position:absolute">
  <defs>
    <symbol id="i-compare" viewBox="0 0 10 10"><path d="M1 3h7M6 1l2 2-2 2M9 7H2M4 5L2 7l2 2" fill="none" stroke="#a8a8a8" stroke-width="1"/></symbol>
    <symbol id="i-trash" viewBox="0 0 10 10"><path d="M1.5 2.5h7M4 2.5V1.3h2v1.2" fill="none" stroke="#a8a8a8" stroke-width="1"/><path d="M2.5 3.5h5l-.5 5.5H3z" fill="#a8a8a8"/><path d="M4.3 4.5v3.5M5.7 4.5v3.5" stroke="#fff" stroke-width=".6"/></symbol>
    <symbol id="i-cart" viewBox="0 0 10 10"><path d="M.5 1.5h1.6l1.2 5h5l1-3.5H2.7" fill="none" stroke="#a8a8a8" stroke-width="1"/><circle cx="3.8" cy="8.4" r=".8" fill="#a8a8a8"/><circle cx="7.6" cy="8.4" r=".8" fill="#a8a8a8"/></symbol>
  </defs>
</svg>

<div class="abs topbar">
  <span class="abs label">Newsletters :</span>
  <span class="abs email">Enter Your Email id :</span>
  <span class="abs join">JOIN NOW</span>
  <div class="abs links">
    <span><svg width="8" height="8" viewBox="0 0 8 8"><circle cx="4" cy="2.5" r="2" fill="#999"/><path d="M0 8c0-3 8-3 8 0z" fill="#999"/></svg>My Account</span>
    <span><svg width="7" height="8" viewBox="0 0 7 8"><rect x="0" y="3.5" width="7" height="4.5" fill="#999"/><path d="M1.5 3.5V2a2 2 0 0 1 4 0v1.5" stroke="#999" fill="none"/></svg>Login</span>
    <span><svg width="9" height="8" viewBox="0 0 9 8"><path d="M0 1h2l1 4h5l1-3H2.5" stroke="#999" fill="none"/><circle cx="3.5" cy="7" r=".9" fill="#999"/><circle cx="7" cy="7" r=".9" fill="#999"/></svg>Shopping Cart : (0) Items</span>
  </div>
</div>

<div class="abs brand"><span class="mark"></span><span class="name">TRAILMARK DEPOT</span></div>

<div class="abs hero" role="img" aria-label="Two hikers with backpacks and trekking poles looking over a green valley">
  <h1 class="abs">TRAILMARK DEPOT</h1>
  <p class="abs">IT IS A LONG ESTABLISHED FACT THAT A READER WILL BE DIS OF A PAGE WHEN LOOKING AT ITS LAYOUT.</p>
  <span class="abs shop">SHOP NOW</span>
  <div class="abs dots"><i></i><i class="on"></i><i></i><i></i></div>
</div>

<nav class="abs nav">
  <a class="active" style="width:70px">HOME</a>
  <a style="width:134px">HUNTING ACCESSORIES</a>
  <a style="width:80px">CAMPING</a>
  <a style="width:69px">FISING</a>
  <a style="width:70px">HIKING</a>
  <a style="width:113px">THIS WEEKS DEALS</a>
  <a style="width:80px;border-right:0">BRANDS</a>
</nav>

<div class="abs shade"></div>

<aside class="abs cats">
  <div class="head"><svg width="11" height="9" viewBox="0 0 11 9" fill="#fff"><rect width="2" height="2"/><rect x="3" width="8" height="2"/><rect y="3.5" width="2" height="2"/><rect x="3" y="3.5" width="8" height="2"/><rect y="7" width="2" height="2"/><rect x="3" y="7" width="8" height="2"/></svg>CATEGORIES</div>
  <ul>
    <li><svg viewBox="0 0 16 16" fill="none" stroke="#333" stroke-width="1.2"><circle cx="4.5" cy="10" r="3.5"/><circle cx="11.5" cy="10" r="3.5"/><path d="M2 7l2-4M14 7l-2-4"/></svg>OPTICS<i class="go"></i></li>
    <li><svg viewBox="0 0 16 16" fill="none" stroke="#333" stroke-width="1.4"><rect x="2" y="2" width="12" height="12" rx="2"/><circle cx="8" cy="8" r="2.5"/></svg>SAFES<i class="go"></i></li>
    <li><svg viewBox="0 0 16 16" fill="none" stroke="#333" stroke-width="1.4"><rect x="3" y="2" width="10" height="6"/><path d="M8 8v6M8 10l-5 4M8 10l5 4"/></svg>BIPOD AND TRIPODS<i class="go"></i></li>
    <li><svg viewBox="0 0 16 16" fill="none" stroke="#333" stroke-width="1.2"><path d="M8 1.5a4.5 4.5 0 0 0-2.5 8.2V12h5V9.7A4.5 4.5 0 0 0 8 1.5zM6 14h4"/></svg>LIGHTS<i class="go"></i></li>
    <li><svg viewBox="0 0 16 16" fill="#333"><path d="M1 5h4l1.5-2h3L11 5h4v9H1z"/><circle cx="8" cy="9.5" r="2.5" fill="#f4f4f4"/></svg>CAMERAS<i class="go"></i></li>
    <li><svg viewBox="0 0 16 16" fill="#333"><path d="M1 13L8 3l7 10z"/><path d="M6.5 13L8 9l1.5 4z" fill="#f4f4f4"/></svg>TENTS<i class="go"></i></li>
    <li><svg viewBox="0 0 16 16" fill="none" stroke="#333" stroke-width="1.5"><path d="M2.5 11V8a5.5 5.5 0 0 1 11 0v3"/><rect x="1.5" y="9.5" width="3" height="5" fill="#333"/><rect x="11.5" y="9.5" width="3" height="5" fill="#333"/></svg>EAR PROTECTION<i class="go"></i></li>
    <li><svg viewBox="0 0 16 16" fill="none" stroke="#333" stroke-width="1.3"><circle cx="8" cy="8" r="6.5"/><circle cx="8" cy="8" r="3.5"/><circle cx="8" cy="8" r="1" fill="#333"/></svg>TARGETS<i class="go"></i></li>
  </ul>
</aside>

<section class="abs brands">
  <h2 class="side-title">OUR BRANDS</h2>
  <ul style="margin-top:8px">
    <li>Corvanta</li><li>Lumelle</li><li>Brisol</li><li>Verantha</li><li>Pelloria Fieldcraft</li><li>Pure Tarova</li>
  </ul>
</section>

<section class="abs loginbox">
  <h2 class="side-title">LOGIN FORM</h2>
  <div class="field">User Name :</div>
  <div class="field">Password :</div>
  <div class="btn">Login</div>
</section>

<h2 class="abs feat-title side-title">FEATURED PRODUCTS</h2>
<div class="abs feat-rule"></div>
<div class="abs feat-arrows"><span>&lsaquo;</span><span>&rsaquo;</span></div>

<div class="abs card" style="left:238px;top:517px">
  <span class="abs photo" role="img" aria-label="Blue and black ear muffs" style="background:radial-gradient(ellipse 34px 38px at 50% 52%,#3d62ad 0%,#2a3f78 45%,rgba(40,55,100,.35) 75%,rgba(255,255,255,0) 100%)"></span>
  <span class="abs badge" style="background:var(--yellow)">New</span>
  <p class="abs name">Halvik Ridge Hearing Protector</p>
  <p class="abs desc">Sed sapien sapien, vulputate ac varius vitae, rutrum ultrices...</p>
  <div class="abs actions"><span><svg><use href="#i-compare"/></svg></span><span><svg><use href="#i-trash"/></svg></span><span><svg><use href="#i-cart"/></svg></span><div class="price"><small>$</small>56<sup>.06</sup></div></div>
</div>
<div class="abs card" style="left:389px;top:517px">
  <span class="abs photo" role="img" aria-label="Black rifle bipod" style="background:radial-gradient(ellipse 22px 40px at 50% 50%,#3a3a3a 0%,#555 45%,rgba(80,80,80,.3) 75%,rgba(255,255,255,0) 100%)"></span>
  <span class="abs badge" style="background:var(--olive)">Sale</span>
  <p class="abs name">Halvik Ridge Hearing Protector</p>
  <p class="abs desc">Sed sapien sapien, vulputate ac varius vitae, rutrum ultrices...</p>
  <div class="abs actions"><span><svg><use href="#i-compare"/></svg></span><span><svg><use href="#i-trash"/></svg></span><span><svg><use href="#i-cart"/></svg></span><div class="price"><small>$</small>56<sup>.06</sup></div></div>
</div>
<div class="abs card" style="left:541px;top:517px">
  <span class="abs photo" role="img" aria-label="Green dome tent" style="background:radial-gradient(ellipse 42px 26px at 50% 58%,#8cbf3a 0%,#6a9a2c 45%,rgba(90,130,40,.3) 75%,rgba(255,255,255,0) 100%)"></span>
  <span class="abs badge" style="background:var(--red)">Off</span>
  <p class="abs name">Halvik Ridge Hearing Protector</p>
  <p class="abs desc">Sed sapien sapien, vulputate ac varius vitae, rutrum ultrices...</p>
  <div class="abs actions"><span><svg><use href="#i-compare"/></svg></span><span><svg><use href="#i-trash"/></svg></span><span><svg><use href="#i-cart"/></svg></span><div class="price"><small>$</small>56<sup>.06</sup></div></div>
</div>
<div class="abs card" style="left:238px;top:722px">
  <span class="abs photo" role="img" aria-label="Black red dot rifle sight" style="background:radial-gradient(ellipse 34px 30px at 50% 55%,#d49a2a 0%,#222 35%,#333 55%,rgba(40,40,40,.3) 78%,rgba(255,255,255,0) 100%)"></span>
  <span class="abs badge" style="background:var(--red)">New</span>
  <p class="abs name">Halvik Ridge Hearing Protector</p>
  <p class="abs desc">Sed sapien sapien, vulputate ac varius vitae, rutrum ultrices...</p>
  <div class="abs actions"><span><svg><use href="#i-compare"/></svg></span><span><svg><use href="#i-trash"/></svg></span><span><svg><use href="#i-cart"/></svg></span><div class="price"><small>$</small>56<sup>.06</sup></div></div>
</div>
<div class="abs card" style="left:389px;top:722px">
  <span class="abs photo" role="img" aria-label="Clear shooting glasses" style="background:radial-gradient(ellipse 44px 16px at 50% 52%,#555 0%,#9a9a9a 40%,rgba(190,190,190,.4) 75%,rgba(255,255,255,0) 100%)"></span>
  <span class="abs badge" style="background:var(--yellow)">Hot</span>
  <p class="abs name">Halvik Ridge Hearing Protector</p>
  <p class="abs desc">Sed sapien sapien, vulputate ac varius vitae, rutrum ultrices...</p>
  <div class="abs actions"><span><svg><use href="#i-compare"/></svg></span><span><svg><use href="#i-trash"/></svg></span><span><svg><use href="#i-cart"/></svg></span><div class="price"><small>$</small>56<sup>.06</sup></div></div>
</div>
<div class="abs card" style="left:541px;top:722px">
  <span class="abs photo" role="img" aria-label="Open black pistol safe case" style="background:radial-gradient(ellipse 40px 30px at 50% 55%,#1a1a1a 0%,#333 50%,rgba(50,50,50,.3) 78%,rgba(255,255,255,0) 100%)"></span>
  <span class="abs badge" style="background:var(--olive)">Off</span>
  <p class="abs name">Halvik Ridge Hearing Protector</p>
  <p class="abs desc">Sed sapien sapien, vulputate ac varius vitae, rutrum ultrices...</p>
  <div class="abs actions"><span><svg><use href="#i-compare"/></svg></span><span><svg><use href="#i-trash"/></svg></span><span><svg><use href="#i-cart"/></svg></span><div class="price"><small>$</small>56<sup>.06</sup></div></div>
</div>

<div class="abs pager"><span class="edge">«</span><span>1</span><span>2</span><span>3</span><span>4</span><span>5</span><span>6</span><span class="cur">7</span><span>8</span><span>9</span><span class="edge">»</span></div>
<div class="abs pager-line"></div>

<footer class="abs footer">
  <div class="abs fcol" style="left:75px"><h3>MY ACCOUNT</h3><ul class="links"><li>My orders</li><li>My credit slips</li><li>My addresses</li><li>My personal info</li></ul></div>
  <div class="abs fcol" style="left:236px"><h3>INFORMATION</h3><ul class="links"><li>My Account</li><li>Order History</li><li>Wish List</li><li>Newsletter</li><li>Specials</li></ul></div>
  <div class="abs fcol" style="left:395px"><h3>CUSTOMER SERVICE</h3><ul class="links"><li>Contact Us</li><li>Returns</li><li>Site Map</li><li>Brands</li><li>Gift Vouchers</li></ul></div>
  <div class="abs fcol" style="left:553px"><h3>CONTACT US</h3>
    <ul class="contact">
      <li><i><svg width="6" height="7" viewBox="0 0 6 7"><path d="M3 7C1 4.5 .5 3.5.5 2.5a2.5 2.5 0 0 1 5 0C5.5 3.5 5 4.5 3 7z" fill="#777"/></svg></i>Address : 250/Lorem ipsum Dummy</li>
      <li><i><svg width="5" height="7" viewBox="0 0 5 7"><rect x=".5" y=".5" width="4" height="6" rx=".8" fill="none" stroke="#777"/></svg></i>(000)-121-1231</li>
      <li><i><svg width="7" height="5" viewBox="0 0 7 5"><rect x=".5" y=".5" width="6" height="4" fill="none" stroke="#777"/><path d="M.5.5l3 2.2 3-2.2" fill="none" stroke="#777"/></svg></i>info@trailmarkdepot.example</li>
    </ul>
  </div>
  <div class="abs fdivider"></div>
  <span class="abs fnews">NEWSLETTER :</span>
  <span class="abs fnews-input">Enter Your Email :<i></i></span>
  <span class="abs follow">FOLLOW US :</span>
  <div class="abs socials">
    <i style="background:#3b5a9a"></i><i style="background:#2fa3e0"></i><i style="background:#f29b1c"></i><i style="background:#d8352c"></i><i style="background:#dc4a38"></i><i style="background:#2c5a8c"></i>
  </div>
</footer>
<div class="abs copy">© Copy Rights 2015 Trailmark Depot.All Rights Reserved.</div>

</body>
</html>
```